Company director needs a business card design

I am a semi-retired former senior finance executive who sits on a number of public and private company boards and do some consulting work. I work largely with emerging businesses but deal regularly with top end of town lawyers, bankers etc. I need a thoughtful but relatively conservative design which would also resonate with my younger client base. Some colour would be good. Information limited to name, address, office tel, mobile and email.

Industry/Entity Type

Finance

```html
<!DOCTYPE html>
<html lang="en">
<head>
<meta charset="utf-8">
<title>Daniel Mercer – Business Card</title>
<link rel="stylesheet" href="https://fonts.googleapis.com/css2?family=Big+Shoulders+Display:wght@300&family=Arimo&display=swap">
<style>
  :root {
    --page-bg: #ffffff;
    --card-bg: #ffffff;
    --card-shadow: rgba(0, 0, 0, 0.45);
    --name-grey: #6f6f6f;
    --bar-grey: #808080;
    --text-grey: #444444;
    --icon-grey: #555555;
  }
  html, body {
    margin: 0;
    padding: 0;
    width: 1200px;
    height: 900px;
    overflow: hidden;
    background: var(--page-bg);
  }
  .canvas {
    position: relative;
    width: 1200px;
    height: 900px;
  }
  .business-card {
    position: absolute;
    left: 29px;
    top: 51px;
    width: 737px;
    height: 419px;
    background: var(--card-bg);
    box-shadow: 6px 8px 14px var(--card-shadow);
  }
  .holder-name {
    position: absolute;
    left: 34px;
    top: 196px;
    margin: 0;
    font-family: "Big Shoulders Display", "Arial Narrow", sans-serif;
    font-weight: 300;
    font-size: 44px;
    line-height: 1;
    letter-spacing: 3px;
    color: var(--name-grey);
    text-transform: uppercase;
    white-space: nowrap;
  }
  .divider-bar {
    position: absolute;
    left: 353px;
    top: 198px;
    width: 15px;
    height: 195px;
    background: var(--bar-grey);
  }
  .contact-list {
    position: absolute;
    left: 378px;
    top: 260px;
    margin: 0;
    padding: 0;
    list-style: none;
    font-family: "Arimo", Arial, sans-serif;
    font-size: 16px;
    color: var(--text-grey);
  }
  .contact-item {
    position: relative;
    height: 20px;
    white-space: nowrap;
  }
  .contact-item svg {
    position: absolute;
    left: 0;
    top: 0;
    width: 22px;
    height: 22px;
    fill: none;
    stroke: var(--icon-grey);
    stroke-width: 1.6;
  }
  .contact-text {
    position: absolute;
    top: 2px;
    line-height: 20px;
  }
  .item-mobile { margin-top: 0; }
  .item-mobile .contact-text { left: 32px; }
  .item-office { margin-top: 16px; }
  .item-office .contact-text { left: 32px; }
  .item-email { margin-top: 14px; }
  .item-email .contact-text { left: 36px; }
  .item-address { margin-top: 18px; }
  .item-address .contact-text { left: 37px; }
</style>
</head>
<body>
<div class="canvas">
  <section class="business-card" aria-label="Business card of Daniel Mercer">
    <h1 class="holder-name">Daniel Mercer</h1>
    <div class="divider-bar"></div>
    <ul class="contact-list">
      <li class="contact-item item-mobile">
        <svg viewBox="0 0 22 22" aria-hidden="true"><rect x="5" y="1" width="11" height="19" rx="1.5"/><line x1="9" y1="17" x2="12" y2="17"/></svg>
        <span class="contact-text">+ 61 400 218 735</span>
      </li>
      <li class="contact-item item-office">
        <svg viewBox="0 0 22 22" aria-hidden="true"><path d="M5 2 L8 2 L9.5 6.5 L7.5 8 C8.5 10.5 10.5 12.5 13 13.5 L14.5 11.5 L19 13 L19 16 C19 17.5 17.5 19 16 19 C9 18 3 12 2 5 C2 3.5 3.5 2 5 2 Z" transform="rotate(-10 11 11)"/></svg>
        <span class="contact-text">+ 61 2 9041 5862</span>
      </li>
      <li class="contact-item item-email">
        <svg viewBox="0 0 22 22" aria-hidden="true"><rect x="1" y="5" width="20" height="12"/><polyline points="1,5 11,12 21,5"/></svg>
        <span class="contact-text">daniel_mercer@northmail.net.au</span>
      </li>
      <li class="contact-item item-address">
        <svg viewBox="0 0 22 22" aria-hidden="true"><path d="M11 20 C7 15 4.5 11.5 4.5 8 A6.5 6.5 0 0 1 17.5 8 C17.5 11.5 15 15 11 20 Z"/><circle cx="11" cy="8" r="2.4"/></svg>
        <span class="contact-text">14 Wattle Grove, Bayside NSW 2099</span>
      </li>
    </ul>
  </section>
</div>
</body>
</html>
```